Website for community Internet Radio station online 24/7

Home page with weather, clock, index, page headings and embedded radio player, and stop press block for moving banner with news.
Pages for schedule, blog, Presenters, new music/video and picture gallery and contact form.
Target Market(s)
Anybody anywhere. Internet around the eorld
Industry/Entity Type
Internet Radio station
Coding
Coded - Design and coding required
Number of Pages Required
5+ page
Font styles to use
Sans Serif
Requirements
Must have
- Embedded music player.

```html
<!DOCTYPE html>
<html lang="en">
<head>
<meta charset="utf-8">
<title>Open Air Radio – Online 24/7</title>
<link href="https://fonts.googleapis.com/css2?family=Montserrat:wght@600;700;800;900&family=Arimo:wght@400;700&display=swap" rel="stylesheet">
<style>
:root{
  --bg:#000;
  --panel:#1b1b1b;
  --panel-2:#2a2a2a;
  --row:#3a3a3a;
  --row-alt:#4a4a4a;
  --orange:#f7821b;
  --teal:#1d7d8c;
  --teal-light:#2aa6b6;
  --white:#fff;
  --muted:#d6d6d6;
  --line:#333;
}
*{box-sizing:border-box;margin:0;padding:0}
html,body{width:1200px;height:4677px;overflow:hidden;background:var(--bg)}
body{position:relative;font-family:"Arimo",Arial,sans-serif;color:var(--white)}
.abs{position:absolute}
.heading{font-family:"Montserrat",sans-serif;font-weight:900;text-transform:uppercase;letter-spacing:.5px;position:relative;display:inline-block;z-index:1}
.heading::after{content:"";position:absolute;left:-8px;right:-8px;top:58%;height:3px;background:var(--teal-light);z-index:-1}
.btn{position:absolute;display:flex;align-items:center;justify-content:center;border-radius:28px;font-family:"Montserrat",sans-serif;font-weight:700;font-size:15px;text-transform:uppercase;color:var(--white)}
.btn-orange{background:var(--orange)}
.btn-teal{background:var(--teal)}

/* header */
.hero-bg{left:0;top:0;width:1200px;height:830px;background:radial-gradient(ellipse at 78% 40%,#1f5566 0%,#0d2630 35%,#07131a 65%,#030608 100%)}
.hero-fade{left:0;top:0;width:1200px;height:830px;background:linear-gradient(90deg,rgba(0,0,0,.55) 0%,rgba(0,0,0,.1) 60%,rgba(0,0,0,0) 100%)}
.follow{left:112px;top:19px;font-size:14px;display:flex;align-items:center;gap:10px}
.follow .dot{width:10px;height:10px;background:var(--white);border-radius:2px}
.login{left:962px;top:18px;font-size:14px}
.clock{left:1022px;top:18px}
.weather{left:1054px;top:12px}
.logo{left:112px;top:70px;width:160px;font-family:"Montserrat",sans-serif;font-weight:800;font-size:13px;color:var(--orange);display:flex;align-items:center;gap:8px}
.logo .mark{width:30px;height:30px;border-radius:50%;background:var(--teal-light);flex:none}
.nav{left:400px;top:89px;display:flex;gap:0;font-size:15px}
.nav a{color:var(--white);text-decoration:none;position:absolute;white-space:nowrap}
.hero-title{left:110px;top:298px;font-family:"Montserrat",sans-serif;font-weight:800;font-size:52px;line-height:62px;text-transform:uppercase}
.hero-text{left:110px;top:438px;width:460px;font-size:15px;line-height:30px}
.play-round{left:856px;top:388px;width:64px;height:64px;border-radius:50%;background:rgba(29,125,140,.85);display:flex;align-items:center;justify-content:center}

/* news */
.news{left:113px;top:767px;width:977px;height:253px;border-radius:22px;overflow:hidden;background:linear-gradient(90deg,#4a3d36 0%,#3a3a3a 40%,#2d2d2d 100%);text-align:center}
.news .heading::after{display:none}
.news h2{margin-top:42px;font-size:31px;font-weight:700;letter-spacing:1px}
.news p{width:720px;margin:22px auto 0;font-size:14.5px;line-height:26px}
.dots{position:absolute;left:450px;top:207px;display:flex;gap:5px}
.dots span{width:10px;height:10px;border-radius:50%;background:var(--orange)}
.dots span.off{background:transparent;border:2px solid var(--orange)}
.ribbon{right:0;top:0;width:120px;height:120px;overflow:hidden}
.ribbon span{position:absolute;right:-38px;top:24px;width:170px;height:30px;transform:rotate(45deg);background:var(--orange);font-size:15px;font-weight:700;text-align:center;line-height:30px}

/* about */
.about-frame{left:113px;top:1103px;width:415px;height:560px;border:5px solid var(--orange);border-radius:30px}
.about-img{left:185px;top:1163px;width:415px;height:562px;border-radius:24px;background:linear-gradient(160deg,#1a4b57 0%,#123845 40%,#0b1c22 70%,#3b2d20 100%)}
.about-title{left:640px;top:1205px;font-size:33px;line-height:48px}
.about-text{left:640px;top:1316px;width:455px;font-size:14.5px;line-height:30px}
.about-link{left:640px;top:1574px;font-family:"Montserrat",sans-serif;font-weight:700;font-size:18px;color:var(--teal-light)}

/* album */
.album-bg{left:0;top:1817px;width:1200px;height:833px;background:radial-gradient(ellipse at 60% 55%,#2b2b2b 0%,#1a1a1a 45%,#0c0c0c 100%)}
.album-heading{left:0;top:1893px;width:1200px;text-align:center;font-size:33px}
.album-frame{left:113px;top:1980px;width:280px;height:270px;border:5px solid var(--teal)}
.disc{left:330px;top:2013px;width:226px;height:270px;border-radius:50%;background:radial-gradient(circle at 36% 50%,#333 0 14px,#eee 15px,#fff 60%,#d9d9d9 100%)}
.album-img{left:148px;top:2013px;width:280px;height:274px;background:linear-gradient(150deg,#6b5a4a 0%,#b06a3a 45%,#3b3330 100%)}
.album-name{left:112px;top:2322px;font-family:"Montserrat",sans-serif;font-weight:700;font-size:24px}
.album-text{left:112px;top:2370px;width:290px;font-size:14.5px;line-height:30px}
.player{left:588px;top:1980px;width:500px;height:585px;background:var(--panel)}
.player-top{left:0;top:0;width:500px;height:140px;background:linear-gradient(90deg,#222 0%,#2f2f2f 100%)}
.thumb{left:16px;top:15px;width:110px;height:104px;background:linear-gradient(150deg,#6b5a4a,#a8683c 50%,#3a3330)}
.thumb-play{left:50px;top:45px;width:36px;height:36px;border-radius:50%;background:var(--white);display:flex;align-items:center;justify-content:center}
.track-title{left:138px;top:18px;font-family:"Montserrat",sans-serif;font-weight:700;font-size:15px}
.track-sub{left:138px;top:48px;font-size:14px}
.controls{left:140px;top:80px;display:flex;align-items:center;gap:16px}
.seek{left:252px;top:90px;width:115px;height:4px;background:#777;border-radius:2px}
.time{right:0;top:110px;font-size:13px;padding-right:4px}
.progress{left:0;top:137px;width:500px;height:6px;background:#3a3a3a}
.progress span{display:block;width:137px;height:6px;background:var(--orange)}
.tracks{left:0;top:147px;width:492px}
.tracks li{list-style:none;height:43.7px;display:flex;align-items:center;justify-content:space-between;padding:0 22px;font-size:14px;background:var(--row);border-bottom:1px solid #2a2a2a}
.tracks li:nth-child(even){background:var(--row-alt)}
.tracks li:first-child{background:#222}
.scrollbar{left:492px;top:147px;width:8px;height:438px;background:var(--white)}
.scrollbar span{position:absolute;left:1px;top:40px;width:6px;height:44px;background:var(--teal)}

/* blog */
.blog-heading{left:0;top:2724px;width:1200px;text-align:center;font-size:33px}
.card{top:2823px;width:315px;height:500px;background:#151515}
.card .photo{height:222px;width:315px}
.card .meta{position:absolute;left:30px;top:243px;right:38px;display:flex;justify-content:space-between;font-size:14.5px}
.card .meta em{font-style:normal;color:var(--orange)}
.card h3{position:absolute;left:20px;right:20px;top:282px;text-align:center;font-family:"Montserrat",sans-serif;font-weight:700;font-size:18px;line-height:30px;text-transform:uppercase}
.card p{position:absolute;left:18px;right:18px;top:350px;text-align:center;font-size:14.5px;line-height:30px}
.card .btn{left:78px;top:482px;width:160px;height:40px}

/* contact */
.contact-bg{left:0;top:3447px;width:1200px;height:743px;background:linear-gradient(180deg,#12303a 0%,#0f3a3f 40%,#123c3a 70%,#0e2226 100%)}
.contact-heading{left:0;top:3552px;width:1200px;text-align:center;font-size:33px}
.field{width:370px;height:44px;border:1px solid #cfd6d8;font-size:14.5px;padding:14px 14px 0}
.field.msg{width:772px;height:174px}
.contact .btn{left:520px;top:4025px;width:160px;height:46px}

/* footer */
.foot-h{top:4293px;font-size:18px;text-align:center}
.foot-col{top:4340px;text-align:center;font-size:13.5px;line-height:40px}
.foot-col .date{color:var(--orange);font-size:12px;line-height:18px}
.news-input{left:465px;top:4410px;width:258px;height:40px;border:1px solid var(--muted);border-radius:4px;font-size:12px;padding:12px 10px;display:flex;justify-content:space-between}
.divider{left:110px;top:4508px;width:980px;height:1px;background:var(--line)}
.copy{left:0;top:4556px;width:1200px;text-align:center;font-size:15px}
.socials{left:556px;top:4603px;display:flex;gap:8px}
.socials span{width:34px;height:34px;border-radius:50%;background:var(--orange)}
</style>
</head>
<body>

<header>
  <div class="abs hero-bg" role="img" aria-label="Recording studio with headphones hanging on a microphone and acoustic foam wall"></div>
  <div class="abs hero-fade"></div>
  <div class="abs follow">Follow Us: <span class="dot"></span><span class="dot"></span><span class="dot"></span><span class="dot"></span></div>
  <div class="abs login">Login</div>
  <svg class="abs clock" width="22" height="22" viewBox="0 0 22 22"><circle cx="11" cy="11" r="9" fill="none" stroke="#fff" stroke-width="2.5"/><path d="M11 6v5h-4" fill="none" stroke="#fff" stroke-width="2"/></svg>
  <svg class="abs weather" width="36" height="32" viewBox="0 0 36 32"><g fill="none" stroke="#fff" stroke-width="1.6"><circle cx="15" cy="12" r="5"/><path d="M15 2v3M5 12h3M8 5l2 2M22 5l-2 2M6 19l2-2"/><path d="M14 28h16a5 5 0 0 0 0-10 7 7 0 0 0-13 2 4 4 0 0 0-3 8z"/></g></svg>
  <div class="abs logo"><span class="mark"></span>OPEN AIR RADIO</div>
  <nav class="abs nav">
    <a style="left:0">Home</a>
    <a style="left:93px">schedule</a>
    <a style="left:207px">Blog</a>
    <a style="left:289px">Presenters</a>
    <a style="left:411px">New music/video</a>
    <a style="left:578px">Gallery</a>
    <a style="left:675px">Contact Us</a>
  </nav>
  <h1 class="abs hero-title">Open Air Radio<br>Online 24/7</h1>
  <p class="abs hero-text">Lorem ipsum dolor sit amet, consectetur adipiscing elit, sed do eiusmod tempor incididunt ut labore et dolore magna</p>
  <div class="btn btn-orange" style="left:110px;top:520px;width:162px;height:55px">Play Music</div>
  <div class="abs play-round"><svg width="14" height="16"><path d="M2 1l11 7-11 7z" fill="#fff"/></svg></div>
</header>

<section class="abs news" role="region" aria-label="Upcoming news">
  <h2 class="heading">Upcoming News</h2>
  <p>Lorem ipsum dolor sit amet, consectetur adipiscing elit, sed do eiusmod tempor incididunt ut labore et dolore magna aliqua. Quis ipsum suspendisse ultrices gravida. Risus commodo viverra maecenas accumsan lacus vel facilisis.</p>
  <div class="dots"><span></span><span class="off"></span><span></span><span></span><span></span></div>
  <div class="abs ribbon"><span>News</span></div>
</section>

<section class="about">
  <div class="abs about-frame"></div>
  <div class="abs about-img" role="img" aria-label="Radio studio control room with mixing desk and lamp"></div>
  <h2 class="abs heading about-title">About Open Air<br>Radio</h2>
  <p class="abs about-text">Lorem ipsum dolor sit amet, consectetur adipiscing elit, sed do eiusmod tempor incididunt ut labore et dolore magna aliqua. Quis ipsum suspendisse ultrices gravida. Risus commodo viverra maecenas accumsan lacus vel facilisis. Lorem ipsum dolor sit amet, consectetur adipiscing elit, sed do eiusmod tempor incididunt ut labore et dolore magna aliqua. Quis ipsum suspendisse ultrices gravida. Risus commodo viverra maecenas accumsan lacus vel facilisis.</p>
  <div class="abs about-link">Learn More</div>
</section>

<section class="album">
  <div class="abs album-bg" role="img" aria-label="Dark mixing console background"></div>
  <div class="abs album-heading"><h2 class="heading">Latest Album</h2></div>
  <div class="abs album-frame"></div>
  <div class="abs disc"></div>
  <div class="abs album-img" role="img" aria-label="Album cover: singer with guitar at a studio microphone"></div>
  <h3 class="abs album-name">Lorem ipsum elit (Lorem ipsum)</h3>
  <p class="abs album-text">Lorem ipsum dolor sit amet, consectetur adipiscing elit, sed do eiusmod tempor incididunt ut labore et dolore magna aliqua. Quis ipsum</p>
  <div class="btn btn-orange" style="left:110px;top:2508px;width:160px;height:48px">Learn More</div>

  <div class="abs player" role="region" aria-label="Music player">
    <div class="abs player-top"></div>
    <div class="abs thumb" role="img" aria-label="Track artwork"></div>
    <div class="abs thumb-play"><svg width="12" height="14"><path d="M1 1l10 6-10 6z" fill="#f7821b"/></svg></div>
    <div class="abs track-title">LOREM IPSUM</div>
    <div class="abs track-sub">Shop</div>
    <div class="abs controls">
      <svg width="12" height="12"><path d="M11 1L2 6l9 5z" fill="#fff"/></svg>
      <svg width="12" height="12"><path d="M2 1l9 5-9 5z" fill="#fff"/></svg>
      <svg width="14" height="12"><path d="M1 4h3l4-3v10L4 8H1z" fill="#fff"/><path d="M10 3a4 4 0 0 1 0 6" stroke="#fff" fill="none"/></svg>
    </div>
    <div class="abs seek"></div>
    <div class="abs time">1:40 &nbsp;/ &nbsp;4:16</div>
    <div class="abs progress"><span></span></div>
    <ul class="abs tracks">
      <li><span>Lorem ipsum</span><span>4:16</span></li>
      <li><span>Lorem ipsum</span><span>4:16</span></li>
      <li><span>Lorem ipsum</span><span>4:16</span></li>
      <li><span>Lorem ipsum</span><span>4:16</span></li>
      <li><span>Lorem ipsum</span><span>4:16</span></li>
      <li><span>Lorem ipsum</span><span>4:16</span></li>
      <li><span>Lorem ipsum</span><span>4:16</span></li>
      <li><span>Lorem ipsum</span><span>4:16</span></li>
      <li><span>Lorem ipsum</span><span>4:16</span></li>
      <li><span>Lorem ipsum</span><span>4:16</span></li>
    </ul>
    <div class="abs scrollbar"><span></span></div>
  </div>
</section>

<section class="blog">
  <div class="abs blog-heading"><h2 class="heading">Latest Blog</h2></div>
  <article class="abs card" style="left:110px">
    <div class="photo" role="img" aria-label="Close-up of mixing desk faders" style="background:linear-gradient(160deg,#2f4a6a,#a8a07a 55%,#3b3b3b)"></div>
    <div class="meta"><span>Dec 21, 2022</span><em>Music</em></div>
    <h3>Lorem ipsum dolor sit amet, consectetur</h3>
    <p>Lorem ipsum dolor sit amet, consectetur adipiscing elit, sed do eiusmod tempor incididunt ut labore et dolore magna aliqua. Quis ipsum</p>
    <div class="btn btn-teal">Learn More</div>
  </article>
  <article class="abs card" style="left:442px">
    <div class="photo" role="img" aria-label="Studio desk with microphone and mixer" style="background:linear-gradient(160deg,#6a3a2a,#2f3f4f 50%,#8a8a8a)"></div>
    <div class="meta"><span>Dec 21, 2022</span><em>Music</em></div>
    <h3>Lorem ipsum dolor sit amet, consectetur</h3>
    <p>Lorem ipsum dolor sit amet, consectetur adipiscing elit, sed do eiusmod tempor incididunt ut labore et dolore magna aliqua. Quis ipsum</p>
    <div class="btn btn-orange">Learn More</div>
  </article>
  <article class="abs card" style="left:773px">
    <div class="photo" role="img" aria-label="Studio microphone over a mixing console" style="background:linear-gradient(160deg,#2a2a2a,#7a7a7a 50%,#1f2a33)"></div>
    <div class="meta"><span>Dec 21, 2022</span><em>Music</em></div>
    <h3>Lorem ipsum dolor sit amet, consectetur</h3>
    <p>Lorem ipsum dolor sit amet, consectetur adipiscing elit, sed do eiusmod tempor incididunt ut labore et dolore magna aliqua. Quis ipsum</p>
    <div class="btn btn-teal">Learn More</div>
  </article>
</section>

<section class="contact">
  <div class="abs contact-bg" role="img" aria-label="Mixing console and headphones tinted teal"></div>
  <div class="abs contact-heading"><h2 class="heading">Contact Us</h2></div>
  <div class="abs field" style="left:198px;top:3663px">Your Name</div>
  <div class="abs field" style="left:599px;top:3663px">Phone</div>
  <div class="abs field" style="left:198px;top:3740px">Address</div>
  <div class="abs field" style="left:599px;top:3740px">Email</div>
  <div class="abs field msg" style="left:198px;top:3817px">Message</div>
  <div class="btn btn-orange">Submit</div>
</section>

<footer>
  <div class="abs foot-h" style="left:110px;width:295px"><h4 class="heading">My Contacts</h4></div>
  <div class="abs foot-h" style="left:442px;width:315px"><h4 class="heading">My Newsletter</h4></div>
  <div class="abs foot-h" style="left:773px;width:315px"><h4 class="heading">Recent Posts</h4></div>

  <div class="abs foot-col" style="left:100px;width:320px">
    <div><svg width="10" height="13" viewBox="0 0 10 13"><path d="M5 0a5 5 0 0 1 5 5c0 4-5 8-5 8S0 9 0 5a5 5 0 0 1 5-5z" fill="#f7821b"/><circle cx="5" cy="5" r="2" fill="#000"/></svg>&nbsp; 12 b Open Air Radio. Lorem ipsum dolor</div>
    <div><svg width="12" height="12" viewBox="0 0 12 12"><path d="M2 0l3 3-2 2a7 7 0 0 0 4 4l2-2 3 3-2 2C5 12 0 7 0 2z" fill="#f7821b"/></svg>&nbsp; 555-014-2270</div>
    <div><svg width="13" height="10" viewBox="0 0 13 10"><rect width="13" height="10" fill="#f7821b"/><path d="M0 0l6.5 5L13 0" stroke="#000" fill="none"/></svg>&nbsp; hello@openairradio.example</div>
  </div>

  <div class="abs foot-col" style="left:455px;width:290px;line-height:30px">Lorem ipsum dolor sit amet, consectetur adipiscing elit</div>
  <div class="abs news-input"><span>Your Email Address</span><svg width="13" height="10" viewBox="0 0 13 10"><rect width="13" height="10" fill="#f7821b"/><path d="M0 0l6.5 5L13 0" stroke="#000" fill="none"/></svg></div>

  <div class="abs foot-col" style="left:773px;width:315px;line-height:20px">
    <div>Lorem ipsum dolor sit amet, consectetur</div>
    <div class="date" style="margin:6px 0 18px">Dec 21, 2022</div>
    <div>Lorem ipsum dolor sit amet, consectetur</div>
    <div class="date" style="margin-top:6px">Dec 21, 2022</div>
  </div>

  <div class="abs divider"></div>
  <div class="abs copy">©Copyrights 2022 Open Air Radio &nbsp;| &nbsp;&nbsp;All Rights Reserved</div>
  <div class="abs socials"><span></span><span></span><span></span></div>
</footer>

</body>
</html>
```